Velmora Skincare packaging designs

We are need to create packaging for our skincare brand. We need two designs. One for round jars which is for creams/capsules and the second will be for bottles/serums Some products will be larger in size so please ensure the packaging design will work and there isn't a lot white/empty space

Below are the names of some of our products.
Screw-On Top Jar (25 pads- 4 inches wide) - Glint Wipes I Skin Brightening Pads
Pump Bottle (2 oz) - ReKINDLE I Hyaluronic Acid + Vitamin Serum
Pump Bottle (6oz) - The Cloud Rinse I Conditioning Face Cleanser
Dropper bottle (1 oz) - Sunny Veil I Hydrating Moisturizer
Cream jar (1.5 oz) - Sunny Veil I Hydrating Moisturizer
Capsules Jar (25 capsules in a jar)- Lumo Burst I Moisture + Hydrating Capsules
Capsules Jar (25 capsules in a jar) - Pure Spark I Impurity Capsules

We will also need help with the packing design in terms of layout of the logo, item name, desc, and ingredients on each product.

Target Market(s)

women

Industry/Entity Type

skincare, beauty

Font styles to use
Sans Serif

Colors
E54698
E96AAD
F1A4CE
F9D9EA
FCEFF6

Requirements
Must have
• Pantone color is 2052 CP HEX #DAAFCA (218 , 175 , 202)

```html
<!DOCTYPE html>
<html lang="en">
<head>
<meta charset="utf-8">
<title>Petal Lab — The Cloud Rinse packaging labels</title>
<link href="https://fonts.googleapis.com/css2?family=Barlow+Condensed:wght@400;500;600&display=swap" rel="stylesheet">
<style>
  :root {
    --bg: #f4f5f6;
    --paper: #ffffff;
    --rose: #e0678a;
    --rose-deep: #d65f80;
    --rose-soft: #e87b9c;
    --silver: #e4e5e7;
    --white: #ffffff;
  }
  * { box-sizing: border-box; margin: 0; padding: 0; }
  html, body { width: 1200px; height: 900px; overflow: hidden; background: var(--bg); }
  body { position: relative; font-family: "Barlow Condensed", "Arial Narrow", sans-serif; }

  .panel { position: absolute; display: flex; flex-direction: column; overflow: hidden; }
  .panel__top { background: var(--paper); display: flex; align-items: center; justify-content: center; }
  .panel__body { background: var(--rose); flex: 1; display: flex; flex-direction: column; align-items: center; color: var(--white); }

  .brand { font-weight: 500; letter-spacing: 0.12em; text-transform: uppercase; color: var(--rose); white-space: nowrap; }
  .brand--light { color: var(--white); }

  .product-name { font-weight: 600; text-transform: uppercase; white-space: nowrap; line-height: 1; }
  .product-rule { height: 2px; background: var(--white); }
  .product-desc { font-weight: 400; text-transform: uppercase; white-space: nowrap; }
  .product-size { font-weight: 400; letter-spacing: 0.2em; }

  /* Pump bottle label */
  .pump-label { left: 87px; top: 358px; width: 262px; height: 400px; }
  .pump-label .panel__top { height: 132px; }
  .pump-label .brand { font-size: 30px; }
  .pump-label .product-name { margin-top: 110px; font-size: 30px; }
  .pump-label .product-rule { width: 212px; margin-top: 6px; }
  .pump-label .product-desc { margin-top: 8px; font-size: 13px; letter-spacing: 0.22em; }
  .pump-label .product-size { margin-top: 66px; font-size: 13px; }

  /* Jar band */
  .jar-band { left: 418px; top: 566px; width: 260px; height: 56px; flex-direction: row; }
  .jar-band .panel__top { width: 93px; background: var(--silver); }
  .jar-band .brand { font-size: 13px; letter-spacing: 0.08em; }
  .jar-band .panel__body { align-items: flex-start; justify-content: center; padding-left: 16px; background: var(--rose-soft); }
  .jar-band .product-name { font-size: 14px; }
  .jar-band .product-rule { width: 98px; height: 1px; margin-top: 3px; }
  .jar-band .product-desc { margin-top: 4px; font-size: 6.5px; letter-spacing: 0.2em; }

  /* Carton face */
  .carton { left: 390px; top: 636px; width: 312px; height: 178px; background: var(--rose-deep); align-items: center; justify-content: center; }
  .carton .brand { font-size: 40px; }

  /* Tube */
  .tube { left: 706px; top: 160px; width: 242px; height: 560px; }
  .tube .panel__top { height: 170px; }
  .tube .brand { font-size: 32px; }
  .tube .product-name { margin-top: 112px; font-size: 26px; }
  .tube .product-rule { width: 170px; margin-top: 6px; }
  .tube .product-desc { margin-top: 8px; font-size: 11.5px; letter-spacing: 0.22em; }
  .tube .product-size { margin-top: 128px; font-size: 16px; }
  .tube-cap { position: absolute; left: 748px; top: 722px; width: 158px; height: 108px; background: var(--paper); }

  /* Dropper label */
  .dropper-label { left: 960px; top: 640px; width: 176px; height: 150px; }
  .dropper-label .panel__top { height: 56px; background: var(--silver); }
  .dropper-label .brand { font-size: 16px; }
  .dropper-label .panel__body { background: var(--rose-deep); }
  .dropper-label .product-name { margin-top: 22px; font-size: 15px; }
  .dropper-label .product-rule { width: 112px; height: 1px; margin-top: 3px; }
  .dropper-label .product-desc { margin-top: 4px; font-size: 7px; letter-spacing: 0.2em; }
  .dropper-label .product-size { margin-top: 10px; font-size: 7px; }
</style>
</head>
<body>

  <section class="panel pump-label" aria-label="Pump bottle label">
    <div class="panel__top"><span class="brand">Petal Lab</span></div>
    <div class="panel__body">
      <h1 class="product-name">The Cloud Rinse</h1>
      <div class="product-rule"></div>
      <p class="product-desc">Conditioning Face Cleanser</p>
      <p class="product-size">6OZ</p>
    </div>
  </section>

  <section class="panel jar-band" aria-label="Jar label band">
    <div class="panel__top"><span class="brand">Petal Lab</span></div>
    <div class="panel__body">
      <h2 class="product-name">The Cloud Rinse</h2>
      <div class="product-rule"></div>
      <p class="product-desc">Conditioning Face Cleanser</p>
    </div>
  </section>

  <section class="panel carton" aria-label="Carton front">
    <span class="brand brand--light">Petal Lab</span>
  </section>

  <section class="panel tube" aria-label="Tube label">
    <div class="panel__top"><span class="brand">Petal Lab</span></div>
    <div class="panel__body">
      <h2 class="product-name">The Cloud Rinse</h2>
      <div class="product-rule"></div>
      <p class="product-desc">Conditioning Face Cleanser</p>
      <p class="product-size">6OZ</p>
    </div>
  </section>
  <div class="tube-cap" aria-hidden="true"></div>

  <section class="panel dropper-label" aria-label="Dropper bottle label">
    <div class="panel__top"><span class="brand">Petal Lab</span></div>
    <div class="panel__body">
      <h2 class="product-name">The Cloud Rinse</h2>
      <div class="product-rule"></div>
      <p class="product-desc">Conditioning Face Cleanser</p>
      <p class="product-size">6OZ</p>
    </div>
  </section>

</body>
</html>
```